Website for Meadowlark Harvest Co

Slogan to be used is Fresh is Best !
I would like the website to be like my other business @ www.tuberworks.com.au. It is the same business

Vegetable Processing

Coded - Design and coding required

1 page

```html
<!DOCTYPE html>
<html lang="en">
<head>
<meta charset="utf-8">
<title>Meadowlark Harvest Co</title>
<link rel="stylesheet" href="https://fonts.googleapis.com/css2?family=Ubuntu:wght@500;700&family=Open+Sans:wght@400;600&display=swap">
<style>
:root{
  --lime:#85ab1c;
  --olive:#617f4e;
  --olive-dark:#5a7648;
  --ink:#1e1e1e;
  --footer:#121212;
  --white:#ffffff;
  --meta:#5f7f4e;
}
*{box-sizing:border-box;margin:0;padding:0}
html,body{width:1200px;height:2589px;overflow:hidden}
body{position:relative;background:var(--white);font-family:"Open Sans",sans-serif;color:var(--ink)}
.abs{position:absolute}
.heading{font-family:"Ubuntu",sans-serif;font-weight:700}

.site-header{left:0;top:0;width:1200px;height:84px;background:var(--white);z-index:3}
.brand{left:110px;top:28px;font-family:"Ubuntu",sans-serif;font-weight:500;font-size:29px;color:var(--lime);letter-spacing:.3px}
.main-nav{left:573px;top:33px;display:flex;gap:23px;font-size:17px}
.main-nav span.active{color:var(--olive)}
.btn{display:flex;align-items:center;justify-content:center;background:var(--lime);color:var(--white);font-weight:600;font-size:16px;clip-path:polygon(0 0,94% 0,100% 100%,6% 100%)}
.btn-quote{left:956px;top:26px;width:132px;height:39px}

.hero{left:0;top:84px;width:1200px;height:545px;background:linear-gradient(100deg,#2f3034 0%,#3c3d42 38%,#2a2b2e 45%,#3f7a1c 58%,#5aa126 78%,#3e7f1a 100%)}
.hero-title{left:110px;top:252px;font-size:59px;color:var(--white);letter-spacing:.5px}
.btn-hero{left:112px;top:337px;width:130px;height:39px}
.wave{left:0;top:530px}

.categories-title{left:109px;top:802px;font-size:47px;line-height:54px}
.categories-title .l1{color:var(--lime)}
.categories-title .l2{color:var(--olive)}
.cat-card{top:704px;width:237px;height:337px}
.cat-label{position:absolute;left:0;right:0;bottom:34px;text-align:center;color:var(--white);font-weight:600;font-size:20px}
.carrot{left:379px;background:radial-gradient(circle at 55% 45%,#f07c2a 0%,#e56a1f 50%,#3c3e44 80%)}
.spinach{left:629px;background:linear-gradient(160deg,#8cba3a,#74a82c 60%,#5e9a24);color:var(--white);text-align:center}
.spinach h3{margin-top:50px;font-size:20px;font-weight:600}
.spinach p{margin:24px 18px 0;font-size:14px;line-height:26px}
.spinach svg{position:absolute;left:108px;bottom:38px}
.peas{left:879px;background:radial-gradient(circle at 50% 40%,#6fae2c 0%,#5a9326 30%,#a2774c 45%,#4a3320 80%)}
.beet{left:1129px;background:radial-gradient(circle at 80% 50%,#8a1f3a 0%,#b03048 30%,#e9e2e2 50%,#c8343e 75%)}

.about{left:0;top:1115px;width:1200px;height:528px;background:var(--olive)}
.about-photo{left:111px;top:1193px;width:370px;height:370px;border-radius:50%;background:radial-gradient(circle at 45% 45%,#e4d9a6 0%,#b9a45a 35%,#5e5a6e 65%,#2c2c2c 100%)}
.about-photo-small{left:315px;top:1385px;width:196px;height:196px;border-radius:50%;border:3px solid var(--lime);background:radial-gradient(circle at 45% 50%,#e0a64c 0%,#d04a2e 40%,#6b8a2a 70%,#5a2d4e 100%)}
.about-title{left:557px;top:1202px;font-size:51px;color:var(--white)}
.about-text{left:557px;top:1274px;width:531px;color:var(--white);font-size:19.5px;line-height:30px;text-align:justify}
.btn-about{left:557px;top:1490px;width:130px;height:39px}

.blogs-title{left:0;top:1718px;width:1200px;text-align:center;font-size:51px;letter-spacing:1px}
.blogs-title .l1{color:var(--lime)}
.blogs-title .l2{color:var(--olive)}
.blog-photo{top:1836px;width:317px;height:250px}
.bp1{left:112px;background:linear-gradient(135deg,#3d4034,#6f8a3a 45%,#c9442b 85%)}
.bp2{left:442px;background:linear-gradient(160deg,#8cc43a,#5f9628 50%,#7a6e5a)}
.bp3{left:772px;background:radial-gradient(circle at 55% 35%,#5f8f2a 0%,#3f6a1e 35%,#5b4030 65%,#8b8076 100%)}
.blog-card{top:2067px;width:302px;height:232px;background:var(--white);border-radius:6px;box-shadow:0 4px 14px rgba(0,0,0,.12);padding:28px 20px 0}
.bc1{left:120px}.bc2{left:450px}.bc3{left:780px}
.blog-meta{font-size:14.5px;color:var(--meta)}
.blog-card h4{margin-top:16px;font-size:19px;font-weight:400}
.blog-card p{margin-top:10px;font-size:16px;line-height:30px;color:#333}

.site-footer{left:0;top:2367px;width:1200px;height:222px;background:var(--footer);color:var(--white);text-align:center}
.footer-brand{margin-top:40px;font-family:"Ubuntu",sans-serif;font-weight:500;font-size:30px}
.footer-nav{margin-top:10px;display:flex;justify-content:center;gap:23px;font-size:18px}
.social{margin-top:18px;display:flex;justify-content:center;gap:17px}
.social span{width:26px;height:26px;border-radius:50%;background:var(--white)}
.copyright{margin-top:14px;font-size:15px}
</style>
</head>
<body>

<header class="site-header abs">
  <div class="brand abs">Meadowlark Harvest Co</div>
  <nav class="main-nav abs"><span class="active">Home</span><span>About</span><span>Vegitables</span><span>Blog</span><span>Contact</span></nav>
  <div class="btn btn-quote abs">Get a quote</div>
</header>

<section class="hero abs" role="img" aria-label="Bowl of fresh peas and spinach leaves on dark stone surface"></section>
<h1 class="hero-title heading abs">Fresh is Best!</h1>
<div class="btn btn-hero abs">Learn More</div>
<svg class="wave abs" width="1200" height="110" viewBox="0 0 1200 110" aria-hidden="true">
  <path d="M0 30 C120 80 260 90 420 60 C520 40 560 20 640 20 C760 20 820 70 960 82 C1060 90 1140 60 1200 35 L1200 110 L0 110 Z" fill="#617d4b"/>
  <path d="M0 60 C120 95 260 95 420 72 C520 56 560 32 640 34 C760 36 820 82 960 92 C1060 99 1140 75 1200 55 L1200 110 L0 110 Z" fill="#e3efd0"/>
  <path d="M0 66 C140 100 270 104 430 80 C530 64 575 40 650 44 C770 50 830 92 965 100 C1065 106 1140 82 1200 66 L1200 110 L0 110 Z" fill="#ffffff"/>
</svg>

<h2 class="categories-title heading abs"><span class="l1">Vegetable</span><br><span class="l2">Categories</span></h2>
<div class="cat-card carrot abs" role="img" aria-label="Sliced carrots in a bowl"><div class="cat-label">Carrot</div></div>
<div class="cat-card spinach abs">
  <h3>Spinach</h3>
  <p>Lorem ipsum dolor sit amet, consectetur adipiscing elit, sed do eiusmod tempor incididunt ut labore et dolore magna.</p>
  <svg width="20" height="14" viewBox="0 0 20 14" aria-hidden="true"><path d="M1 7H18M12 1l6 6-6 6" stroke="#fff" stroke-width="1.6" fill="none"/></svg>
</div>
<div class="cat-card peas abs" role="img" aria-label="Green peas in a wooden bowl"><div class="cat-label">Peas</div></div>
<div class="cat-card beet abs" role="img" aria-label="Diced beetroot on a checked cloth"></div>

<section class="about abs"></section>
<div class="about-photo abs" role="img" aria-label="Roasted cauliflower and vegetables"></div>
<div class="about-photo-small abs" role="img" aria-label="Bowl of mixed fresh salad vegetables"></div>
<h2 class="about-title heading abs">About Us</h2>
<div class="about-text abs">
  <p>Lorem ipsum dolor sit amet, consectetur adipiscing elit, sed do eiusmod tempor incididunt ut labore et dolore magna aliqua. Quis ipsum suspendisse ultrices gravida.</p>
  <p style="margin-top:4px">Lorem ipsum dolor sit amet, consectetur adipiscing elit, sed do eiusmod tempor incididunt ut labore et dolore magna aliqua. Quis ipsum suspendisse ultrices gravida.</p>
</div>
<div class="btn btn-about abs">Learn More</div>

<h2 class="blogs-title heading abs"><span class="l1">Latest</span> <span class="l2">Blogs</span></h2>
<div class="blog-photo bp1 abs" role="img" aria-label="Table of dips, olives and vegetable sticks"></div>
<div class="blog-photo bp2 abs" role="img" aria-label="Fresh celery stalks in a glass bowl"></div>
<div class="blog-photo bp3 abs" role="img" aria-label="Broccoli florets in a dark bowl"></div>
<article class="blog-card bc1 abs"><div class="blog-meta">25-01-2022 &nbsp;|&nbsp; By Clara Wendt</div><h4>Sed ut perspiciatis unde omnis</h4><p>Sed ut perspiciatis unde omnis iste natus error sit voluptatem accusant ium doloremque</p></article>
<article class="blog-card bc2 abs"><div class="blog-meta">25-01-2022 &nbsp;|&nbsp; By Clara Wendt</div><h4>Sed ut perspiciatis unde omnis</h4><p>Sed ut perspiciatis unde omnis iste natus error sit voluptatem accusant ium doloremque</p></article>
<article class="blog-card bc3 abs"><div class="blog-meta">25-01-2022 &nbsp;|&nbsp; By Clara Wendt</div><h4>Sed ut perspiciatis unde omnis</h4><p>Sed ut perspiciatis unde omnis iste natus error sit voluptatem accusant ium doloremque</p></article>

<footer class="site-footer abs">
  <div class="footer-brand">Meadowlark Harvest Co</div>
  <nav class="footer-nav"><span>Home</span><span>About</span><span>Vegitables</span><span>Blog</span><span>Contact</span></nav>
  <div class="social"><span></span><span></span></div>
  <div class="copyright">2023 Meadowlark Harvest Co.All Rights Reserved.</div>
</footer>

</body>
</html>
```